Flyer-Design für verschiedene Anwendungsfälle bzw. Produkte
Zielgruppe
Wir lösen reale Probleme mit digitalen Technologien wie IoT und KI. In unseren Projekten liefern wir Gesamtlösungen von der Strategieberatung über Konzepterstellung bis zur technischen Umsetzung und dem Betrieb. Integration und Konzeption spielen eine große Rolle, wir sind kein Hardwareanbieter, sondern bauen Komplettlösungen aus Software, Connectivity und Hardware. Unsere Kunden sind gehobener Mittelstand bis Konzern, ab 25 Mio € aufwärts. Oft sind unsere Kunden aus konservativen Branchen. Wir müssen beim Design immer einen Kompromiss aus innovativ und Vertrauen erweckend finden. Unsere Persona ist weiß, männlich, über 50, nicht besonders technologieaffin.
Aufgabenstellung
Wir brauchen eine Flyer-Vorlage für verschiedene Anwendungsfälle bzw. Produkte. Im Anhang sind Beispiele für Produktbeschreibungen, sowie ein Flyer, den wir selbst designet haben.
Ergebnis soll ein Flyer-Design sein, das wir für solche Produkte immer wieder verwenden können, DIN A5 zweiseitig.
Exo2 und Trebuchet sind unsere Schriftarten. Logos habe ich in 2 Formaten angehängt.
Website: tavolu.me
Wenn Sie weitere Ideen haben, sind wir ganz Ohr.
Grafisch bitte nur die Farben grau, schwarz und orange verwenden (grau und orange siehe Logo)

```html
<!DOCTYPE html>
<html lang="de">
<head>
<meta charset="utf-8">
<title>Tavolu Flyer – Füllstandsüberwachung</title>
<link href="https://fonts.googleapis.com/css2?family=Montserrat:wght@400;500;600;700;800&display=swap" rel="stylesheet">
<style>
  :root{
    --orange:#e8792a;
    --orange-deep:#dd6a1f;
    --navy:#1f2a3a;
    --ink:#1b1b1b;
    --text:#2e2e2e;
    --grey-bg:#e6e6e6;
    --paper:#ffffff;
  }
  *{box-sizing:border-box;margin:0;padding:0}
  html,body{width:1200px;height:900px;overflow:hidden;background:var(--grey-bg)}
  body{font-family:"Montserrat",sans-serif;color:var(--text);position:relative}

  .page{position:absolute;top:75px;width:530px;height:750px;background:var(--paper);overflow:hidden;box-shadow:0 6px 18px rgba(0,0,0,.12)}
  .page--front{left:43px}
  .page--back{left:627px}

  /* front */
  .network-backdrop{position:absolute;left:0;top:0;width:100%;height:360px;
    background:radial-gradient(ellipse at 40% 35%,#cfcfcf 0%,#ececec 45%,#fafafa 80%)}
  .headline{position:absolute;left:52px;top:46px;font-weight:800;font-size:44px;line-height:1.05;color:var(--ink)}
  .subline{position:absolute;left:52px;top:200px;font-weight:700;font-size:20px;line-height:1.25;color:var(--orange)}
  .brand{position:absolute;right:48px;top:150px;display:flex;align-items:center;gap:8px;
    font-weight:600;font-size:26px;letter-spacing:4px;color:var(--orange)}
  .brand__dot{width:12px;height:12px;border-radius:50%;background:var(--orange)}

  .case{position:absolute;font-size:12.5px;line-height:1.4}
  .case--one{left:0;top:320px;width:270px;height:430px;background:linear-gradient(160deg,var(--orange) 0%,var(--orange-deep) 100%);
    color:#fff;padding:40px 22px 0 40px}
  .case--two{left:290px;top:288px;width:226px;color:var(--text)}
  .case__label{font-weight:700;font-size:14px;margin-bottom:6px}
  .case--two .case__label{color:var(--orange)}
  .case__intro{margin-bottom:8px}
  .case--one .case__intro{margin-bottom:12px}
  .case--two .case__intro{color:var(--orange)}
  .case__list{list-style:none}
  .case__list li::before{content:"- "}

  .contact-bar{position:absolute;left:0;bottom:0;width:100%;height:120px}
  .contact-bar svg.shape{position:absolute;left:0;top:0}
  .contact{position:absolute;display:flex;align-items:center;gap:8px;color:#fff;font-size:12.5px}
  .contact__icon{width:20px;height:20px;border-radius:50%;background:#fff;display:flex;align-items:center;justify-content:center}
  .contact--phone{left:40px;bottom:16px}
  .contact--address{left:262px;top:20px}
  .contact--mobile{left:262px;top:50px}
  .contact--mail{left:262px;top:80px}

  /* back */
  .band-top{position:absolute;left:0;top:0;width:100%;height:34px;background:var(--navy)}
  .band-bottom{position:absolute;left:0;bottom:0;width:100%;height:72px;background:var(--navy);
    display:flex;align-items:center;justify-content:center;color:#fff;font-weight:700;font-size:15px;letter-spacing:.5px}
  .section{position:absolute;left:40px;width:450px;text-align:center;font-size:12.5px;line-height:1.5}
  .section__title{display:inline-block;background:var(--orange);color:#fff;font-weight:700;font-size:15px;padding:3px 16px;margin-bottom:10px}
  .section--function{top:58px}
  .section--hardware{top:296px;border:2px solid var(--orange);padding:0 18px 18px;height:220px}
  .section--hardware .section__title{margin-top:-14px}
  .section--frontend{top:530px}
  .section p{margin-bottom:4px}
  .sensor-row{display:flex;justify-content:space-around;align-items:flex-end;margin-top:14px}
  .sensor{border-radius:10px;background:linear-gradient(180deg,#4a4a4a,#1c1c1c)}
  .sensor--pair{width:100px;height:50px}
  .sensor--round{width:90px;height:62px;background:linear-gradient(135deg,#2a2a2a 40%,#3fa9a0 70%,#e8e8e8)}
  .sensor--flat{width:100px;height:44px}
</style>
</head>
<body>

<section class="page page--front" aria-label="Vorderseite">
  <div class="network-backdrop" role="img" aria-label="Dezente graue Netzwerkgrafik aus verbundenen Punkten"></div>

  <h1 class="headline">LoRaWAN<br>oder<br>NB-IoT:</h1>
  <p class="subline">Füllstandsüberwachung<br>und Routenoptimierung<br>Abfallwirtschaft</p>

  <div class="brand"><span class="brand__dot"></span>TAVOLU</div>

  <div class="case case--one">
    <p class="case__label">Fall 1:</p>
    <p class="case__intro">große öffentliche Container, z.B. Altglas, Altkleider, Altpapier Nutzen und Vorteile</p>
    <ul class="case__list">
      <li>Bürger wissen, zu welchen Containern sie ihren Abfall bringen können</li>
      <li>Entsorger kann optimiert leeren und Kosten sparen</li>
      <li>Containerstandorte können datengestützt erweitert oder reduziert werden</li>
      <li>Weniger wilder Müll</li>
    </ul>
  </div>

  <div class="case case--two">
    <p class="case__label">Fall 2:</p>
    <p class="case__intro">Kleinere städtische Mülleimer, z.B. in Erholungsgebieten Nutzen und Vorteile</p>
    <ul class="case__list">
      <li>Nutzung der Mülleimer ist stark von unregelmäßigen Faktoren wie Wetter oder Veranstaltungen abhängig</li>
      <li>Starr regelmäßige Leerung führt häufig zu Überfüllung und dadurch Umweltverschmutzung, die durch die Anwendung von Sensoren vermieden wird</li>
      <li>Überflüssige Leerungen werden vermieden und dadurch Kosten gespart</li>
    </ul>
  </div>

  <div class="contact-bar">
    <svg class="shape" width="530" height="120" viewBox="0 0 530 120">
      <path d="M0 70 H225 L245 0 H530 V120 H0 Z" fill="#1f2a3a"/>
    </svg>
    <div class="contact contact--phone"><span class="contact__icon"><svg width="12" height="12" viewBox="0 0 24 24"><path d="M6.6 10.8a15 15 0 0 0 6.6 6.6l2.2-2.2a1 1 0 0 1 1-.25 11 11 0 0 0 3.6.6 1 1 0 0 1 1 1V20a1 1 0 0 1-1 1A17 17 0 0 1 3 4a1 1 0 0 1 1-1h3.5a1 1 0 0 1 1 1 11 11 0 0 0 .6 3.6 1 1 0 0 1-.25 1z" fill="#1f2a3a"/></svg></span>0211 4400210</div>
    <div class="contact contact--address"><span class="contact__icon"><svg width="12" height="12" viewBox="0 0 24 24"><path d="M12 3 2 12h3v8h5v-5h4v5h5v-8h3z" fill="#1f2a3a"/></svg></span>Hafenweg 8, 40210 Musterstadt</div>
    <div class="contact contact--mobile"><span class="contact__icon"><svg width="12" height="12" viewBox="0 0 24 24"><rect x="7" y="2" width="10" height="20" rx="2" fill="#1f2a3a"/><rect x="9" y="5" width="6" height="11" fill="#fff"/></svg></span>+49 170 2288341</div>
    <div class="contact contact--mail"><span class="contact__icon"><svg width="12" height="12" viewBox="0 0 24 24"><rect x="3" y="6" width="18" height="12" rx="1" fill="#1f2a3a"/><path d="M3 7l9 6 9-6" stroke="#fff" stroke-width="1.6" fill="none"/></svg></span>consulting@tavolu.me</div>
  </div>
</section>

<section class="page page--back" aria-label="Rückseite">
  <div class="band-top"></div>

  <div class="section section--function">
    <h2 class="section__title">Funktionsweise</h2>
    <p>-Im Container werden Sensoren zur Füllstandsmessung angebracht.</p>
    <p>- Der Füllstand wird an eine Bürger-Website/ -App gemeldet, die nur „voll", „fast voll" und „nicht voll" anzeigt, sowie bei voll oder fast voll eine möglichst nahe gelegene Alternative.</p>
    <p>- Der Füllstand wird an den Entsorger gemeldet. Hier kann entweder eine Routenoptimierungs-App zur Verfügung gestellt oder die Daten in ein bestehendes Betriebsführungssystem integriert werden.</p>
    <p>- Die Daten werden analysiert, um die regelmäßige Auslastung der Container zu bestimmen und ihre Standorte langfristig zu optimieren.</p>
  </div>

  <div class="section section--hardware">
    <h2 class="section__title">Hardware</h2>
    <p>Ultraschall-, Radar- oder optische Sensoren messen den Abstand zwischen sich selbst und der Oberfläche und erkennen so den Füllstand</p>
    <div class="sensor-row">
      <div class="sensor sensor--pair" role="img" aria-label="Produktfoto: zwei kompakte schwarze Füllstandssensoren"></div>
      <div class="sensor sensor--round" role="img" aria-label="Produktfoto: Sensor mit rundem Messfenster"></div>
      <div class="sensor sensor--flat" role="img" aria-label="Produktfoto: flacher schwarzer Radarsensor"></div>
    </div>
  </div>

  <div class="section section--frontend">
    <h2 class="section__title">Frontend und Benachrichtigungen</h2>
    <p>-Darstellung in einer Web App (für Mobilgeräte und PCs) auf einer Karte für Bürger, mit Anzeige von Alternativen bei vollen Containern</p>
    <p>- Einbindung in Routenoptimierungs- oder Betriebsführungs-Anwendung beim Entsorger</p>
    <p>- Alarmierung bei Überschreitung von Grenzwerten möglich</p>
  </div>

  <div class="band-bottom">www.tavolu.me</div>
</section>

</body>
</html>
```